依頼詳細
ラフではありますが、pptでチラシ案を作成しました。
要望事項も記載しておりますので、内容のご確認をお願いいたします。
不明点御座いましたら、お気軽にお申し付けください。
記載項目
記載事項もチラシ案に記載しております。
内容のご確認をお願いいたします。
不明点御座いましたら、お気軽にお申し付けください。
サイズ
A4
ページ数
両面
希望イメージ
シンプル 複雑
単色 カラフル
暗い 明るい
日常 高級
遊び心 厳粛
未来的 伝統的
女性的 男性的
希望する色
青系、無彩色系
納品ファイル
• イラストレーター形式 (.ai)
• PNG形式 (.png)
補足説明
aiとpdfでいただけますと幸いです。
ラフ案作成済です。体裁を整えていただく依頼となります。

本件のポイントを的確に捉えて表現いただいたことが決め手になりました。また、全体的なバランスと見やすさを加味して選定をさせていただだきました。

この度は、沢山の素晴らしいご提案をくださいまして、誠にありがとうございました。 素人が作成したラフ案から、こちらの意図を汲み取っていただき、どれも素晴らしい内容で、選考にはとても苦慮いたしましたが、慎重に皆様の提案を一つ一つ確認し、検討させていただきました。 お忙しい中、ご提案頂きましたこと皆様に重ねてお礼申し上げます。 次回ご提案をお願いさせていただく際もよろしくお願いいたします。

```html
<!DOCTYPE html>
<html lang="ja">
<head>
<meta charset="utf-8">
<title>RR × PPA 自家消費PPAのご案内</title>
<link rel="stylesheet" href="https://fonts.googleapis.com/css2?family=Noto+Sans+JP:wght@400;500;700;900&display=swap">
<style>
:root{
  --blue:#1f6fc2;
  --blue-dark:#114f96;
  --blue-light:#cfe4f7;
  --sky:#e8f2fb;
  --red:#e0262b;
  --ink:#333;
  --grey:#8a8f96;
  --white:#fff;
  --green:#2f9e58;
}
*{margin:0;padding:0;box-sizing:border-box}
html,body{width:849px;height:1200px;overflow:hidden;background:var(--white)}
body{font-family:"Noto Sans JP",sans-serif;color:var(--ink);position:relative}
.abs{position:absolute}

.brand-row{top:18px;left:0;width:849px;height:50px}
.brand{position:absolute;display:flex;align-items:center;gap:8px;font-weight:700;color:var(--blue-dark)}
.brand-left{left:34px;top:10px;font-size:20px}
.brand-left .mark{width:22px;height:22px;background:var(--blue);border-radius:50%}
.brand-mid{left:330px;top:10px;font-size:15px}
.brand-mid .mark{width:22px;height:22px;background:var(--blue);border-radius:50%}
.badge{position:absolute;right:30px;top:4px;width:110px;height:40px;background:var(--green);border-radius:4px}

.lead-bar{top:74px;left:60px;width:729px;height:34px;background:var(--blue);color:var(--white);
  font-size:18px;font-weight:700;text-align:center;line-height:34px;letter-spacing:.04em}

.headline{top:120px;left:0;width:849px;text-align:center;font-size:17px;font-weight:500}
.headline .first{color:var(--red);font-size:34px;font-weight:900;margin-right:24px;vertical-align:-4px}

.hero{top:160px;left:0;width:849px;height:120px;font-weight:900;color:var(--blue);font-size:128px;line-height:120px}
.hero .rr{position:absolute;left:100px;letter-spacing:.02em}
.hero .x{position:absolute;left:365px;font-size:84px;font-weight:500}
.hero .ppa{position:absolute;left:460px;letter-spacing:.02em}
.term{top:290px;font-size:10px;color:var(--grey)}
.term-rr{left:118px}
.term-ppa{left:480px}

.zero-row{top:310px;left:60px;width:740px;display:flex;justify-content:space-between;align-items:baseline}
.zero-item{font-size:20px;font-weight:700;color:var(--blue-dark)}
.zero-item b{font-size:52px;font-weight:900;color:var(--blue);margin-left:10px}

.photos{top:392px;left:42px;width:765px;display:flex;gap:12px}
.photo-cell{flex:1;text-align:center}
.photo{height:118px;background:linear-gradient(135deg,#8b6a4f,#b3927a 55%,#6f665f)}
.photo.grey{background:linear-gradient(135deg,#9a9ea3,#c9c3b8 55%,#857d72)}
.photo-cell p{font-size:12px;margin-top:6px}

.solve{top:552px;left:0;width:849px;text-align:center;font-size:18px;font-weight:700;color:var(--blue)}
.consult{top:584px;left:0;width:849px;text-align:center;font-size:18px;font-weight:700;color:var(--red)}

.solution-band{top:630px;left:0;width:849px;height:40px;background:var(--blue);color:var(--white);
  font-size:18px;font-weight:700;line-height:40px;padding-left:46px}

.flow{top:690px;left:0;width:849px;height:490px}
.flow svg{position:absolute;left:0;top:0}
.zero-box{position:absolute;left:255px;top:38px;color:var(--white);font-size:13px;font-weight:700;line-height:1.4}
.zero-box b{position:absolute;left:110px;top:2px;font-size:58px;font-weight:900;line-height:1}
.partner-mark{position:absolute;left:50px;top:150px;display:flex;align-items:center;gap:8px;font-size:13px;font-weight:700;color:var(--blue-dark);width:180px}
.partner-mark .mark{width:22px;height:22px;border-radius:50%;background:var(--blue);flex:none}
.points{position:absolute;left:250px;top:150px;color:var(--red);font-size:18px;font-weight:700;line-height:1.7}
.pay-box{position:absolute;left:190px;top:255px;width:430px;height:34px;background:var(--blue-light);
  color:var(--blue-dark);font-size:13px;font-weight:700;text-align:center;line-height:34px}
.building{position:absolute;left:640px;top:10px;width:170px;height:340px;
  background:linear-gradient(180deg,#3a86d4,#1b5ea8)}
.pill{position:absolute;top:380px;height:36px;width:160px;border-radius:18px;background:var(--blue);
  color:var(--white);font-size:15px;font-weight:700;text-align:center;line-height:36px}
.pill-left{left:40px}
.pill-right{left:645px}
.contract{position:absolute;left:350px;top:388px;font-size:11px;color:var(--white);font-weight:700}
</style>
</head>
<body>

<header class="abs brand-row">
  <div class="brand brand-left"><span class="mark"></span>彩光テクノロジー</div>
  <div class="brand brand-mid"><span class="mark"></span>あおばエナジーパートナーズ</div>
  <div class="badge" role="img" aria-label="認定バッジ"></div>
</header>

<div class="abs lead-bar">太陽光設置に興味はあるけど屋根の劣化で諦めているお客様へ</div>

<p class="abs headline"><span class="first">業界初！！</span>初期投資0円ではじめる、自家消費PPA</p>

<h1 class="abs hero"><span class="rr">RR</span><span class="x">×</span><span class="ppa">PPA</span></h1>
<p class="abs term term-rr">（Roof Repair：屋根補修）</p>
<p class="abs term term-ppa">（Power Purchase Agreement 電力購入契約）</p>

<div class="abs zero-row">
  <span class="zero-item">屋根補修<b>0</b>円</span>
  <span class="zero-item">太陽光発電設置<b>0</b>円</span>
  <span class="zero-item">保守管理費用<b>0</b>円</span>
</div>

<div class="abs photos">
  <figure class="photo-cell"><div class="photo" role="img" aria-label="錆びた屋根の写真"></div><p>錆びている</p></figure>
  <figure class="photo-cell"><div class="photo" role="img" aria-label="錆びた折板屋根の写真"></div><p>錆びている</p></figure>
  <figure class="photo-cell"><div class="photo grey" role="img" aria-label="割れ欠けのあるスレート屋根の写真"></div><p>割れ、欠けがある</p></figure>
  <figure class="photo-cell"><div class="photo grey" role="img" aria-label="劣化した屋根の写真"></div><p>劣化している</p></figure>
</div>

<p class="abs solve">RR（屋根補修）×PPA（イニシャル費ゼロの太陽光）がそんなお悩みを解決します！！</p>
<p class="abs consult">重塩害地域で設置が困難なお客様もご相談ください！</p>

<div class="abs solution-band">RR×PPAは屋根補修と太陽光発電システムを組み合わせた新しいソリューションです。</div>

<section class="abs flow">
  <svg width="849" height="490" viewBox="0 0 849 490" aria-hidden="true">
    <defs>
      <linearGradient id="flowArrow" x1="0" x2="1" y1="0" y2="0">
        <stop offset="0" stop-color="#5aa7e6"/>
        <stop offset="1" stop-color="#1f6fc2"/>
      </linearGradient>
    </defs>
    <path d="M40 130 Q60 40 230 30 L600 30 L600 5 L640 60 L600 115 L600 90 L240 90 Q120 95 100 130 Z" fill="url(#flowArrow)"/>
    <polygon points="210,360 630,360 630,350 645,366 630,382 630,372 210,372" fill="var(--blue)"/>
  </svg>
  <div class="zero-box">屋根補修<br>太陽光発電設置<br>保守管理<b>0円</b></div>
  <div class="partner-mark"><span class="mark"></span>あおばエナジー<br>パートナーズ</div>
  <div class="points">・環境対策と屋根補修が一度に実現!!<br>・電気代高騰の今がチャンス!!</div>
  <div class="pay-box">削減された分の電気料金を支払い（契約期間20年）</div>
  <div class="building" role="img" aria-label="お客様の建物のイラスト"></div>
  <div class="pill pill-left">PPA事業者</div>
  <div class="pill pill-right">お客様</div>
  <span class="contract" style="top:342px;color:var(--blue-dark)">PPA契約</span>
</section>

</body>
</html>
```